Plakat-Design (LED-Wand) für Heizung-/Sanitär- und Klimatechnik
Zielgruppe
Heizung Sanitär und Klimatechnik
Aufgabenstellung
Wir möchten Regional in unserer Stadt auf einer LED Wand werben.
Unser Logo soll vertreten sein und unsere Telefonnummer. Da es auf den Winter zu geht wollen wir darauf aufmerksam machen, dass wir z.B. bei einem Heizungsausfall/Reparatur ein Ansprechpartner sind. z.B.: Heizung kalt? Wir machen es Ihnen warm ums Herz!
Gerne auch eigene Ideen.
Stockbilder können gerne mit eingebracht werden. Ist aber kein Muss.
Die Anzeige auf der LED Wand beträgt 6 Sekunden. Diese befindet sich auf einer Straßenverkehrskreuzung. Es soll also nicht überladen sein. Das Logo (Symbol und Schriftzug, kann wenn erforderlich auch nebeneinander gesetzt werden)
Anforderung der LED Wand: 800x600px 72dpi als JPG.

```html
<!DOCTYPE html>
<html lang="de">
<head>
<meta charset="utf-8">
<title>Heizung kalt? – LED-Wand Plakatvarianten</title>
<link href="https://fonts.googleapis.com/css2?family=Titan+One&family=Luckiest+Guy&family=Open+Sans:wght@400;700;800&display=swap" rel="stylesheet">
<style>
  :root{
    --page:#eef0f2;
    --label:#3a3f45;
    --poster-bg:#ffffff;
    --ice-blue:#2f6fb8;
    --ice-light:#9cc8ee;
    --deep-blue:#1d4f8f;
    --warm-top:#ffcf1f;
    --warm-bottom:#f07a12;
    --grey-text:#6b7178;
    --band-line:#2f6fb8;
  }
  *{margin:0;padding:0;box-sizing:border-box}
  html,body{width:1200px;height:931px;overflow:hidden;background:var(--page)}
  body{position:relative;font-family:"Open Sans",Arial,sans-serif}

  .variant-label{position:absolute;font-family:"Open Sans",Arial,sans-serif;font-weight:800;font-size:54px;color:var(--label)}
  .poster{position:absolute;width:520px;height:390px;background:var(--poster-bg);overflow:hidden;box-shadow:0 2px 8px rgba(0,0,0,.15)}
  .poster--illustration{left:80px;top:40px}
  .poster--pet{left:660px;top:40px}
  .poster--couple{left:390px;top:500px}

  .headline{position:absolute;left:28px;top:16px;font-family:"Titan One",Impact,sans-serif;font-size:44px;letter-spacing:1px;
    background:linear-gradient(180deg,var(--ice-light) 0%,var(--ice-blue) 55%,var(--deep-blue) 100%);
    -webkit-background-clip:text;background-clip:text;color:transparent;-webkit-text-stroke:1px var(--deep-blue);z-index:2}
  .subline{position:absolute;left:232px;top:70px;font-size:13px;font-style:italic;color:var(--grey-text);z-index:2}

  .scene{position:absolute;left:20px;top:92px;width:300px;height:215px}
  .poster--illustration .scene{background:radial-gradient(ellipse at 45% 55%,#d9c9a4 0%,#8fb06a 45%,#ffffff 78%)}
  .poster--pet .scene{left:14px;width:492px;height:222px;background:linear-gradient(135deg,#c9a27a 0%,#9b7250 50%,#e6d6bf 100%)}
  .poster--couple .scene{left:14px;width:492px;height:222px;background:linear-gradient(120deg,#8d8a86 0%,#6f5a48 45%,#d2c6b8 100%)}

  .warm-claim{position:absolute;left:352px;top:96px;font-family:"Luckiest Guy",Impact,sans-serif;font-size:48px;line-height:1.02;text-align:center;
    background:linear-gradient(180deg,var(--warm-top) 0%,var(--warm-bottom) 100%);
    -webkit-background-clip:text;background-clip:text;color:transparent;-webkit-text-stroke:1px #c85a0a;z-index:2}

  .contact-band{position:absolute;left:0;right:0;bottom:0;height:70px;background:var(--poster-bg);border-top:3px solid var(--band-line);
    display:flex;align-items:center;justify-content:space-between;padding:0 22px}
  .brand{display:flex;align-items:center;gap:8px;font-weight:700;font-size:16px;color:var(--deep-blue)}
  .brand-dot{width:30px;height:30px;border-radius:50%;background:var(--deep-blue)}
  .phone{font-family:"Open Sans",Arial,sans-serif;font-weight:800;font-size:30px;color:var(--deep-blue);letter-spacing:.5px}
</style>
</head>
<body>

  <div class="variant-label" style="left:22px;top:40px">2</div>
  <section class="poster poster--illustration">
    <h1 class="headline">HEIZUNG KALT?</h1>
    <p class="subline">…wir machen Ihnen</p>
    <div class="scene" role="img" aria-label="Illustration: frierende Figur mit Mütze und Schal umarmt einen Heizkörper"></div>
    <p class="warm-claim">WARM<br>UMS<br>HERZ!</p>
    <footer class="contact-band">
      <div class="brand"><span class="brand-dot"></span>thermhaus</div>
      <div class="phone">0 21 47 / 36 82 0-50</div>
    </footer>
  </section>

  <div class="variant-label" style="left:602px;top:40px">3</div>
  <section class="poster poster--pet">
    <h1 class="headline">HEIZUNG KALT?</h1>
    <p class="subline">…wir machen Ihnen</p>
    <div class="scene" role="img" aria-label="Foto: Hund eingekuschelt unter einer warmen Wolldecke"></div>
    <p class="warm-claim">WARM<br>UMS<br>HERZ!</p>
    <footer class="contact-band">
      <div class="brand"><span class="brand-dot"></span>thermhaus</div>
      <div class="phone">0 21 47 / 36 82 0-50</div>
    </footer>
  </section>

  <div class="variant-label" style="left:332px;top:500px">4</div>
  <section class="poster poster--couple">
    <h1 class="headline">HEIZUNG KALT?</h1>
    <p class="subline">…wir machen Ihnen</p>
    <div class="scene" role="img" aria-label="Foto: Paar in Decken gehüllt mit heißen Tassen auf dem Sofa"></div>
    <p class="warm-claim">WARM<br>UMS<br>HERZ!</p>
    <footer class="contact-band">
      <div class="brand"><span class="brand-dot"></span>thermhaus</div>
      <div class="phone">0 21 47 / 36 82 0-50</div>
    </footer>
  </section>

</body>
</html>
```